Cedar Hall letterhead

We changed our name and logo now need letterhead.
3-4/72 Harlow Street Marlow Vale 2163
www.cedarhall.org.au
info@cedarhall.org.au
ph: 02 97584120

At this stage, we are preferencing Design #: 5398880 and Design #5401338

```html
<!DOCTYPE html>
<html lang="en">
<head>
<meta charset="utf-8">
<title>Cedar Hall Letterhead</title>
<link rel="stylesheet" href="https://fonts.googleapis.com/css2?family=Cinzel:wght@600;700&display=swap">
<style>
  :root {
    --ink: #111418;
    --brand: #5f8597;
    --band-deep: #7b9eaf;
    --band-mid: #b3c8d2;
    --paper: #ffffff;
  }
  html, body {
    margin: 0;
    padding: 0;
    overflow: hidden;
    background: var(--paper);
  }
  .letterhead {
    position: relative;
    width: 927px;
    height: 1200px;
    overflow: hidden;
    background: var(--paper);
    font-family: "Cinzel", Georgia, serif;
    color: var(--ink);
  }
  .brand-name {
    position: absolute;
    left: 54px;
    top: 89px;
    width: 108px;
    margin: 0;
    text-align: center;
    font-size: 19px;
    font-weight: 600;
    line-height: 1.1;
    letter-spacing: 1px;
    color: var(--brand);
  }
  .contact {
    position: absolute;
    left: 152px;
    top: 55px;
    margin: 0;
    padding: 0;
    list-style: none;
  }
  .contact li {
    position: absolute;
    left: 0;
    white-space: nowrap;
    font-weight: 700;
  }
  .contact .address {
    top: 0;
    font-size: 13px;
    letter-spacing: 3.3px;
  }
  .contact .web,
  .contact .email {
    left: 26px;
    font-size: 13px;
    letter-spacing: 4.6px;
  }
  .contact .web { top: 29px; }
  .contact .email { top: 59px; }
  .contact .phone {
    top: 87px;
    font-size: 15px;
    letter-spacing: 3.6px;
  }
  .contact .phone .label {
    font-size: 12px;
    letter-spacing: 3px;
  }
  .footer-band {
    position: absolute;
    left: 0;
    bottom: 0;
    width: 927px;
    height: 160px;
  }
</style>
</head>
<body>
  <main class="letterhead">
    <h1 class="brand-name">CEDAR<br>HALL</h1>

    <ul class="contact">
      <li class="address">3-4/72 Harlow Street Marlow Vale 2163</li>
      <li class="web">www.cedarhall.org.au</li>
      <li class="email">info@cedarhall.org.au</li>
      <li class="phone"><span class="label">ph:</span> 02 97584120</li>
    </ul>

    <svg class="footer-band" viewBox="0 1040 927 160" aria-hidden="true">
      <defs>
        <linearGradient id="bandFill" x1="0" y1="0" x2="1" y2="0">
          <stop offset="0" stop-color="var(--band-deep)"/>
          <stop offset="0.45" stop-color="var(--band-mid)"/>
          <stop offset="0.9" stop-color="var(--paper)"/>
        </linearGradient>
      </defs>
      <path d="M0,1120 Q463,1045 927,1120 L927,1200 L0,1200 Z" fill="url(#bandFill)"/>
    </svg>
  </main>
</body>
</html>
```